Business Card Design needed for start up company Pramora

In need of a new business card designed for a start up company based in Sydney, Pramora is a new start up innovative Company, our mission it to make property accessible for everyday Australian and to become the leading Real Estate platform in Australia. We want it to be fresh and clean.

Industry/Entity Type

Financial

Contact Information for Business Card

Section for Name
Section for Title

PRAMORA - Where Doors Open Wide
Mobile:
Direct:

Font styles to use
Sans Serif

Colors
33a6d7
0692cd
0255a3
ffffff

Requirements
Must have
• Logo, all business card details

```html
<!DOCTYPE html>
<html lang="en">
<head>
<meta charset="utf-8">
<title>Pramora Business Card</title>
<link href="https://fonts.googleapis.com/css2?family=Roboto+Condensed:wght@300;400;700&display=swap" rel="stylesheet">
<style>
  :root {
    --sky: #33a6d7;
    --ocean: #0692cd;
    --navy: #0255a3;
    --bar: #0a90cb;
    --ink: #1a1a1a;
    --paper: #ffffff;
    --frame: #1a1a1a;
  }
  * { margin: 0; padding: 0; box-sizing: border-box; }
  html, body { width: 1200px; height: 1200px; overflow: hidden; background: var(--paper); }
  body { position: relative; font-family: "Roboto Condensed", "Arial Narrow", sans-serif; color: var(--ink); }

  .card {
    position: absolute;
    left: 118px;
    width: 900px;
    height: 540px;
    border: 2.5px solid var(--frame);
    background: var(--paper);
    overflow: hidden;
  }
  .card--front { top: 42px; }
  .card--back { top: 616px; }

  .wave { position: absolute; left: 0; top: 0; width: 100%; height: 100%; }

  .identity {
    position: absolute;
    left: 0;
    width: 392px;
    text-align: center;
    font-weight: 300;
    line-height: 1;
  }
  .identity__title { top: 126px; font-size: 52px; font-weight: 400; letter-spacing: 0.5px; }
  .identity__company { top: 194px; font-size: 36px; letter-spacing: -0.5px; }

  .timeline {
    position: absolute;
    left: 474px;
    top: 0;
    width: 7px;
    height: 368px;
    background: var(--navy);
  }
  .contact-dot {
    position: absolute;
    left: 454px;
    width: 48px;
    height: 48px;
    border-radius: 50%;
    background: var(--navy);
    display: flex;
    align-items: center;
    justify-content: center;
  }
  .contact-dot svg { width: 26px; height: 26px; }

  .contact-text {
    position: absolute;
    font-size: 17px;
    font-weight: 400;
    line-height: 1;
    transform: translateY(-50%);
    white-space: nowrap;
  }

  .stripe { position: absolute; height: 25px; background: var(--bar); }

  .brand {
    position: absolute;
    left: 0;
    right: 0;
    top: 180px;
    height: 176px;
    display: flex;
    align-items: center;
    justify-content: center;
  }
  .brand__name {
    font-size: 132px;
    font-weight: 700;
    color: var(--navy);
    line-height: 1;
    letter-spacing: 1px;
  }
</style>
</head>
<body>

<section class="card card--front">
  <svg class="wave" viewBox="0 0 900 540" preserveAspectRatio="none" role="img" aria-label="Soft blue wave decoration along the lower edge">
    <defs>
      <linearGradient id="waveFill" x1="0" y1="0" x2="0" y2="1">
        <stop offset="0" stop-color="#0692cd"/>
        <stop offset="1" stop-color="#33a6d7"/>
      </linearGradient>
    </defs>
    <path fill="url(#waveFill)" d="M0,404 C50,318 110,286 174,286 C236,286 275,302 320,326 C480,406 590,466 704,466 C784,466 840,424 900,385 L900,540 L0,540 Z"/>
  </svg>

  <h1 class="identity identity__title">TITLE</h1>
  <p class="identity identity__company">COMPANY NAME</p>

  <div class="timeline"></div>

  <div class="contact-dot" style="top:67px">
    <svg viewBox="0 0 24 24"><path fill="#000" d="M6.6 10.8c1.4 2.8 3.8 5.1 6.6 6.6l2.2-2.2c.3-.3.7-.4 1-.2 1.1.4 2.3.6 3.6.6.6 0 1 .4 1 1V20c0 .6-.4 1-1 1C10.6 21 3 13.4 3 4c0-.6.4-1 1-1h3.5c.6 0 1 .4 1 1 0 1.3.2 2.5.6 3.6.1.3 0 .7-.2 1L6.6 10.8z"/></svg>
  </div>
  <div class="contact-dot" style="top:159px">
    <svg viewBox="0 0 24 24"><path fill="#000" d="M2 10 L12 3 L22 10 V21 H2 Z"/><path fill="none" stroke="#1f5fa8" stroke-width="1.2" d="M2 10 L12 16 L22 10 M2 21 L9 14 M22 21 L15 14"/></svg>
  </div>
  <div class="contact-dot" style="top:249px">
    <svg viewBox="0 0 24 24"><path fill="#000" d="M12 2C8.1 2 5 5.1 5 9c0 5.2 7 13 7 13s7-7.8 7-13c0-3.9-3.1-7-7-7zm0 9.5a2.5 2.5 0 1 1 0-5 2.5 2.5 0 0 1 0 5z"/></svg>
  </div>
  <div class="contact-dot" style="top:343px">
    <svg viewBox="0 0 24 24" fill="none" stroke="#000" stroke-width="1.8"><circle cx="12" cy="12" r="9.5"/><ellipse cx="12" cy="12" rx="4.2" ry="9.5"/><path d="M2.5 12h19M4 7h16M4 17h16M12 2.5v19"/></svg>
  </div>

  <p class="contact-text" style="left:518px; top:90px">1800 000 000 000</p>
  <p class="contact-text" style="left:682px; top:90px">1800 000 000 000</p>
  <p class="contact-text" style="left:518px; top:183px">hello@pramora.com.au</p>
  <p class="contact-text" style="left:523px; top:271px">Location</p>
  <p class="contact-text" style="left:521px; top:364px">Website</p>
</section>

<section class="card card--back">
  <div class="stripe" style="left:0; top:86px; width:340px"></div>
  <div class="stripe" style="left:0; top:129px; width:576px"></div>

  <div class="brand">
    <span class="brand__name">PRAMORA</span>
  </div>

  <div class="stripe" style="left:325px; top:391px; right:0"></div>
  <div class="stripe" style="left:562px; top:433px; right:0"></div>
</section>

</body>
</html>
```